This project is to address Personal Life issues/ Health & Wellness using a certified Professional Coaching Approach.

Major coaching areas include: Weight loss, Overwhelm/ Time Management, Increased Energy, Leadership, Improved Relationships, Finding Your Life Purpose & passion, Self Esteem & Confidence,

The combination of a board certified Internal Medicine physician and
professional coach is a powerful and unique approach to help people achieve
better health and well being.

Target Market(s)

Existing or potentially new patients/clients interested in any of the listed categories of coaching.

Industry/Entity Type

Life Coaching

Font styles to use
Sans Serif

Colors
00a990
0292cd
0255a3
33b8a4
a64599
6b449b
876aae
3176b5
33a6d7

Requirements
Must have
• Design specifics: Use of deep blues/greens using nature imagery is
• preferred- see our website for at Brightvalecare.com
• Each category of coaching must be listed out with a paragraph of description below each- I will provide the description in an attachment that is pending.
• Title of Brochure: "Clearbrook Health Personal Life & Wellness Coaching."
• "Coaching That Works!"
Nice to have
• A definition of coaching on the front of brochure:
• " A compassionate catalyzing relationship - The art of facilitating the performance, learning and development of another so they may achieve what the want faster.”
• Also on the front please place: "Stuck? Ask about a free coaching consult with Dr. Tavren to learn more!"
Should not have
• Should not have anything in the brochure that mentions medical services from the website outside of weight loss. The purpose of the brochure is to promote the coaching services.

```html
<!DOCTYPE html>
<html lang="en">
<head>
<meta charset="utf-8">
<title>Clearbrook Health – Personal Life &amp; Wellness Coaching Brochure</title>
<link href="https://fonts.googleapis.com/css2?family=Open+Sans:ital,wght@0,400;0,600;0,700;1,400&family=Raleway:wght@500;700;800&display=swap" rel="stylesheet">
<style>
  :root{
    --teal:#00a990;
    --teal-light:#33b8a4;
    --sky:#0292cd;
    --sky-light:#33a6d7;
    --navy:#0255a3;
    --blue-mid:#3176b5;
    --plum:#6b449b;
    --violet:#876aae;
    --magenta:#a64599;
    --ink:#3a3a3a;
    --paper:#ffffff;
    --page:#f2f2f2;
  }
  *{box-sizing:border-box;margin:0;padding:0}
  html,body{width:814px;height:1200px;overflow:hidden}
  body{background:var(--page);font-family:"Open Sans",Arial,sans-serif;color:var(--ink);position:relative}
  .spread{position:absolute;left:10px;width:794px;height:574px;display:flex;box-shadow:0 1px 4px rgba(0,0,0,.25);background:var(--paper)}
  .spread--outside{top:8px}
  .spread--inside{top:614px}
  .panel{position:relative;width:264.67px;height:100%;display:flex;flex-direction:column;overflow:hidden}
  .panel + .panel{border-left:1px solid #e3e3e3}

  .tab{display:inline-block;align-self:flex-start;font-family:"Raleway",sans-serif;font-weight:700;font-size:9px;color:#fff;padding:5px 22px 5px 10px;border-radius:0 0 12px 0}
  .tab--green{background:linear-gradient(90deg,var(--teal),var(--teal-light))}
  .tab--purple{background:linear-gradient(90deg,var(--plum),var(--violet))}
  .tab--blue{background:linear-gradient(90deg,var(--navy),var(--sky-light))}
  .tab--inline{margin-top:8px}

  .copy{padding:6px 12px 0 12px;font-size:7.2px;line-height:1.5}
  .copy p{margin-bottom:5px}
  .copy strong{color:var(--navy)}
  .bullets{list-style:none;padding:6px 12px 0 12px;font-size:7.2px;line-height:1.5}
  .bullets li{padding-left:9px;position:relative;margin-bottom:2px}
  .bullets li::before{content:"";position:absolute;left:0;top:3.5px;width:4px;height:4px;border-radius:50%;background:var(--teal)}
  .tagline{padding:6px 12px;font-style:italic;font-size:8.5px;color:var(--navy);font-weight:600}

  .footer-bar{margin-top:auto;height:26px;display:flex;align-items:center;justify-content:center;font-size:7px;color:#fff;font-weight:600;background:linear-gradient(90deg,var(--teal),var(--teal-light))}
  .footer-bar--blue{background:linear-gradient(90deg,var(--navy),var(--sky))}

  .photo{width:100%;flex:none}

  /* Outside front: services */
  .services{background:linear-gradient(180deg,var(--sky) 0%,var(--navy) 100%);color:#fff}
  .services__title{font-family:"Raleway",sans-serif;font-weight:700;font-size:14px;text-align:center;padding:14px 0 10px}
  .services__grid{display:grid;grid-template-columns:1fr 1fr;gap:10px 14px;padding:0 22px}
  .service{text-align:center;font-size:6.8px;line-height:1.3}
  .service__image{height:62px;border-radius:6px;border:2px solid rgba(255,255,255,.85);margin-bottom:3px}
  .service--center{grid-column:1 / span 2;width:96px;justify-self:center}

  /* Cover */
  .cover__head{background:linear-gradient(180deg,var(--plum),var(--violet));color:#fff;padding:22px 14px 14px;text-align:right}
  .cover__brand{font-family:"Raleway",sans-serif;font-weight:700;font-size:19px;line-height:1.2}
  .cover__subtitle{font-family:"Raleway",sans-serif;font-weight:500;font-size:12px;margin-top:3px}
  .cover__badge{display:inline-block;background:#fff;color:var(--plum);font-family:"Raleway",sans-serif;font-weight:800;font-size:16px;padding:6px 12px;margin-top:12px}
  .cover__bar{font-size:6.6px;background:linear-gradient(90deg,var(--teal),var(--sky));}

  /* Inside right title block */
  .title-block{background:linear-gradient(180deg,var(--sky-light),var(--blue-mid));color:#fff;text-align:center;padding:20px 12px;margin-top:10px}
  .title-block__brand{font-family:"Raleway",sans-serif;font-weight:700;font-size:18px}
  .title-block__subtitle{font-family:"Raleway",sans-serif;font-weight:500;font-size:11px;margin-top:4px}
</style>
</head>
<body>

<!-- Outside spread -->
<section class="spread spread--outside">
  <div class="panel">
    <span class="tab tab--green">Why Coaching?</span>
    <div class="copy">
      <p>There is a <strong>strong connection</strong> between personal fulfillment and health. Coaching gives you the structure, support and accountability to turn good intentions into lasting change.</p>
      <p>Coaching is a compassionate, professional relationship that helps the individual achieve what they want faster.</p>
    </div>
    <div class="photo" style="height:330px;margin-top:auto;background:linear-gradient(180deg,#cfe6ee 0%,#a9cfae 55%,#6f9d5a 100%)" role="img" aria-label="Smiling woman jogging outdoors in bright sunlight"></div>
    <div class="footer-bar" style="margin-top:0">Brightvalecare.com</div>
  </div>

  <div class="panel services">
    <h2 class="services__title">Coaching Services</h2>
    <div class="services__grid">
      <div class="service"><div class="service__image" style="background:linear-gradient(135deg,#e7e2d8,#b9c8c0)" role="img" aria-label="Measuring tape around a waist"></div>1. Weight Loss</div>
      <div class="service"><div class="service__image" style="background:linear-gradient(135deg,#d9d9d9,#8ea3b5)" role="img" aria-label="Clock face for time management"></div>2. Overwhelm &amp; Time Management</div>
      <div class="service"><div class="service__image" style="background:linear-gradient(135deg,#9ccbe8,#e9c77d)" role="img" aria-label="Person leaping with energy at sunset"></div>3. Increased Energy</div>
      <div class="service"><div class="service__image" style="background:linear-gradient(135deg,#f3d1a0,#7a6a59)" role="img" aria-label="Figure standing on a summit"></div>4. Leadership</div>
      <div class="service"><div class="service__image" style="background:linear-gradient(135deg,#e8c9b5,#a48a7a)" role="img" aria-label="Couple holding hands"></div>5. Improved Relationships</div>
      <div class="service"><div class="service__image" style="background:linear-gradient(135deg,#8fb7d9,#4d7f5d)" role="img" aria-label="Open road leading toward a horizon"></div>6. Finding Your Life Purpose</div>
      <div class="service service--center"><div class="service__image" style="background:linear-gradient(135deg,#f0e0c8,#c3a487)" role="img" aria-label="Confident woman with arms raised"></div>7. Confidence/Self Esteem</div>
    </div>
    <div class="footer-bar footer-bar--blue">Brightvalecare.com</div>
  </div>

  <div class="panel">
    <header class="cover__head">
      <div class="cover__brand">Clearbrook Health</div>
      <div class="cover__subtitle">Personal Life &amp; Wellness Coaching</div>
      <div class="cover__badge">THAT WORKS!</div>
    </header>
    <div class="photo" style="flex:1;background:linear-gradient(180deg,#f6cf8a 0%,#c9a6cf 40%,#8a62b0 75%,#5a3f86 100%)" role="img" aria-label="Lavender field stretching toward a sunrise sky"></div>
    <div class="footer-bar cover__bar" style="margin-top:0">Ask about a free coaching consult with Dr. Tavren</div>
  </div>
</section>

<!-- Inside spread -->
<section class="spread spread--inside">
  <div class="panel">
    <span class="tab tab--green">Weight Loss</span>
    <div class="copy">
      <p>Two thirds of American adults are over weight or obese, putting themselves at risk for preventable illness. A steady plan and a coach who listens can help you reach a healthy weight you keep.</p>
      <p>Fad diets don't work. Sustainable weight loss requires a holistic approach that addresses your habits, your stress and your environment.</p>
    </div>
    <span class="tab tab--green tab--inline">Leadership</span>
    <div class="copy">
      <p>We look first to lead ourselves before we can lead others. Effective leadership grows from clarity, purpose and the courage to act on what matters most.</p>
    </div>
    <div class="tagline">Master your fear… master your life!</div>
    <div class="photo" style="flex:1;background:linear-gradient(180deg,#bfe3f3 0%,#7cc3df 45%,#e7d6b4 100%)" role="img" aria-label="Woman relaxing on a sunny beach"></div>
    <div class="footer-bar" style="margin-top:0">Brightvalecare.com</div>
  </div>

  <div class="panel">
    <span class="tab tab--purple">Overwhelm &amp; Time Management</span>
    <ul class="bullets">
      <li>Do you feel as if your plate is overflowing?</li>
      <li>Overwhelmed and stressed at work, family and personal needs?</li>
      <li>Is managing time a constant struggle?</li>
      <li>Busy but not productive?</li>
      <li>Tired?</li>
    </ul>
    <div class="copy"><p>All of these have a negative effect on your health and happiness. Coaching helps you set priorities and reclaim your time.</p></div>
    <span class="tab tab--purple tab--inline">Increased Energy</span>
    <div class="copy"><p>Increased energy is a byproduct of lifestyle changes that create better sleep, nutrition, movement and a calmer mind. Small steps build momentum.</p></div>
    <span class="tab tab--purple tab--inline">Improved Relationships</span>
    <div class="copy"><p>There are time tested principles to renew relationships. Many of those we coach have found new closeness, trust and calm in their homes and workplaces.</p></div>
    <span class="tab tab--purple tab--inline">Confidence/Self Esteem</span>
    <div class="copy"><p>When we suffer from low confidence we hold ourselves back. Coaching helps you see your strengths and step forward with belief.</p></div>
    <div class="footer-bar footer-bar--blue">Brightvalecare.com</div>
  </div>

  <div class="panel">
    <span class="tab tab--blue">Finding Your Life Purpose</span>
    <div class="copy">
      <p>In a world that moves fast, it is easy to lose sight of what truly matters. Coaching helps you uncover your values and build a life with passion and meaning.</p>
      <p><strong>It's your life. Let's discover what you were meant to do.</strong></p>
    </div>
    <div class="title-block">
      <div class="title-block__brand">Clearbrook Health</div>
      <div class="title-block__subtitle">Personal Life &amp; Wellness Coaching</div>
    </div>
    <div class="photo" style="flex:1;background:linear-gradient(180deg,#9fcbe8 0%,#d8e6ee 45%,#8c8a7c 100%)" role="img" aria-label="Man sitting on a rock overlooking the ocean"></div>
    <div class="footer-bar footer-bar--blue" style="margin-top:0"></div>
  </div>
</section>

</body>
</html>
```